Mobile phone signal boosting solutions needs a website

We need a website design for the reselling of a mobile signal boosting product set. These solutions are Travik exempt and will provide an indoor signal for mobile phones. We would like to see designs that incorporate the colours and feel of our logo. The domain will be
nestorbolt.com / co.uk
Overview of the company and how it is to be used: Nestor Bolt (domain name) will work with business and end user to provide mobile signal boosting – where people struggle indoors with a mobile signal our solutions will help by finding the smallest signal and boosting it, allowing users to use voice and data over their mobile network (please note this is not wireless signal boosting)
Number of Pages:
-Home
-Solutions / How it works
-Case Studies
-Contact
Text content: Currently just use placeholders
Technical specs : Wordpress and ability to use CMS if that’s relevant
Target Market(s)
Business professional all markets /high end residential
Coding
Coded - Design and coding required
Number of Pages Required
4 page
Look and feel

```html
<!DOCTYPE html>
<html lang="en">
<head>
<meta charset="utf-8">
<title>Nestor Bolt – Contact</title>
<link rel="stylesheet" href="https://fonts.googleapis.com/css2?family=Roboto+Condensed:wght@400;700&family=Open+Sans:wght@600&display=swap">
<style>
  :root {
    --page-dark: #0a0804;
    --footer-black: #000000;
    --signal-yellow: #ffc20e;
    --text-white: #ffffff;
    --text-muted: #cfcfcf;
    --field-white: #ffffff;
    --rule-grey: #3a3a3a;
    --gutter-grey: #c3c3c3;
    --scroll-track: #4a4a4a;
    --scroll-thumb: #6b6b6b;
    --note-red: #e0201b;
  }
  * { box-sizing: border-box; margin: 0; padding: 0; }
  html, body { width: 1200px; height: 938px; overflow: hidden; }
  body {
    position: relative;
    background: var(--gutter-grey);
    font-family: "Roboto Condensed", "Arial Narrow", sans-serif;
    color: var(--text-white);
  }
  .site { position: absolute; left: 0; top: 0; width: 1044px; height: 938px; }
  .contact-section { position: absolute; left: 0; top: 0; width: 1044px; height: 652px; background: var(--page-dark); }
  .accent-line { position: absolute; left: 843px; top: 0; width: 21px; height: 652px; background: var(--signal-yellow); }

  .brand { position: absolute; display: flex; align-items: center; gap: 7px; }
  .brand-mark { flex: none; background: var(--signal-yellow); }
  .brand-name { font-weight: 400; color: var(--text-white); white-space: nowrap; }
  .site-header .brand { left: 34px; top: 48px; }
  .site-header .brand-mark { width: 12px; height: 12px; }
  .site-header .brand-name { font-size: 17px; line-height: 20px; }

  .main-nav { position: absolute; top: 51px; left: 163px; display: flex; gap: 25px; font-size: 11.5px; }
  .main-nav a { color: var(--text-white); text-decoration: none; }

  .page-title { position: absolute; left: 63px; top: 143px; font-size: 48px; font-weight: 700; line-height: 56px; letter-spacing: 0.3px; }
  .contact-email { position: absolute; left: 63px; top: 204px; font-size: 23.5px; line-height: 30px; color: var(--text-white); text-decoration: underline; text-decoration-thickness: 1.5px; text-underline-offset: 2px; }

  .contact-form { position: absolute; left: 63px; top: 269px; width: 681px; }
  .field-label { display: block; font-size: 11px; line-height: 14px; margin-bottom: 9px; }
  .field-input { display: block; width: 681px; height: 28px; border: none; background: var(--field-white); box-shadow: inset 0 0 4px rgba(0,0,0,0.25); margin-bottom: 10px; }
  .submit-button {
    position: absolute; left: 303px; top: 213px; width: 74px; height: 40px;
    border: none; border-radius: 20px; background: var(--field-white);
    font-family: inherit; font-size: 14px; font-weight: 700; color: #000;
  }

  .site-footer { position: absolute; left: 0; top: 652px; width: 1044px; height: 286px; background: var(--footer-black); }
  .footer-column { position: absolute; top: 36px; }
  .footer-column h3 { font-size: 12px; font-weight: 700; line-height: 16px; margin-bottom: 13px; }
  .footer-column.company h3 { font-weight: 400; }
  .footer-column a { display: block; font-size: 11px; line-height: 16px; margin-bottom: 13.5px; color: var(--text-muted); text-decoration: none; }
  .footer-column.product { left: 34px; }
  .footer-column.company { left: 192px; }
  .footer-column.legal { left: 329px; }
  .site-footer .brand { right: 35px; top: 76px; }
  .site-footer .brand-mark { width: 14px; height: 14px; }
  .site-footer .brand-name { font-size: 20px; line-height: 24px; }
  .footer-rule { position: absolute; left: 34px; top: 178px; width: 975px; height: 1px; background: var(--rule-grey); }
  .copyright { position: absolute; left: 34px; top: 216px; font-size: 11px; color: var(--text-muted); }
  .social-links { position: absolute; left: 934px; top: 217px; display: flex; gap: 16px; }
  .social-links span { width: 13px; height: 13px; border-radius: 50%; background: var(--text-white); }

  .scrollbar { position: absolute; left: 1044px; top: 0; width: 7px; height: 938px; background: var(--scroll-track); }
  .scrollbar-thumb { position: absolute; left: 1px; top: 6px; width: 5px; height: 304px; background: var(--scroll-thumb); }

  .design-note { position: absolute; left: 1052px; top: 218px; }
  .design-note svg { position: absolute; left: 0; top: 3px; }
  .design-note p { position: absolute; left: 47px; top: 0; width: 100px; font-family: "Open Sans", Arial, sans-serif; font-weight: 600; font-size: 10.5px; line-height: 14px; color: var(--note-red); }
</style>
</head>
<body>
  <div class="site">
    <section class="contact-section">
      <header class="site-header">
        <div class="brand">
          <span class="brand-mark"></span>
          <span class="brand-name">Nestor Bolt</span>
        </div>
        <nav class="main-nav">
          <a href="#">How It Works</a>
          <a href="#">Case Studies</a>
          <a href="#">Contact</a>
        </nav>
      </header>

      <h1 class="page-title">Drop us a line!</h1>
      <a class="contact-email" href="#">info@nestorbolt.com</a>

      <form class="contact-form">
        <label class="field-label" for="name">Name</label>
        <input class="field-input" id="name" type="text">
        <label class="field-label" for="email">Email Address</label>
        <input class="field-input" id="email" type="email">
        <label class="field-label" for="message">Message</label>
        <input class="field-input" id="message" type="text">
        <button class="submit-button" type="button">Submit</button>
      </form>

      <div class="accent-line"></div>
    </section>

    <footer class="site-footer">
      <div class="footer-column product">
        <h3>Product</h3>
        <a href="#">How it works</a>
        <a href="#">Case studies</a>
      </div>
      <div class="footer-column company">
        <h3>Company</h3>
        <a href="#">Address</a>
        <a href="#">Contact</a>
      </div>
      <div class="footer-column legal">
        <h3>Legal</h3>
        <a href="#">Privacy Policy</a>
        <a href="#">Terms &amp; Conditions</a>
        <a href="#">Cookies</a>
      </div>
      <div class="brand">
        <span class="brand-mark"></span>
        <span class="brand-name">Nestor Bolt</span>
      </div>
      <div class="footer-rule"></div>
      <p class="copyright">© Nestor Bolt. All rights reserved.</p>
      <div class="social-links" aria-label="Social links">
        <span></span><span></span><span></span>
      </div>
    </footer>
  </div>

  <div class="scrollbar"><div class="scrollbar-thumb"></div></div>

  <div class="design-note">
    <svg width="44" height="10" viewBox="0 0 44 10">
      <line x1="4" y1="5" x2="42" y2="5" stroke="#e0201b" stroke-width="1.2"/>
      <path d="M0 5 L6 2 L6 8 Z" fill="#e0201b"/>
    </svg>
    <p>Animated line to callback to home page.</p>
  </div>
</body>
</html>
```